Travel Blogger Business Card for roamquill.net

I need a two-sided business card for a travel blogging website. The card should be both professional and fun at the same time. This is for the website www.roamquill.net

I don't necessarily think that the current logo on the website needs to be used on the business card but it can be. I am very flexible with ideas

Target Market(s)

Travel agencies that will be met at a conference.

Industry/Entity Type

Travel

Contact Information for Business Card

Company Name: Roam Quill.net
Name: Bertrand Olesky
Voice: +1-(345)-402-7731
Address: Coral Reach Shore, Grand Cayman, Cayman Islands
Email: ceo@roamquill.net

Colors
0592cd
0355a3
3176b5
33a6d7
85cae6
85acd3

Requirements
Must have
• Website address and name should be bigger than address, phone number, and email.

```html
<!DOCTYPE html>
<html lang="en">
<head>
<meta charset="utf-8">
<title>Roam Quill.net – Business Card</title>
<link rel="stylesheet" href="https://fonts.googleapis.com/css2?family=Jost:wght@400;500;700&display=swap">
<style>
  :root {
    --sky: #33a6d7;
    --ocean: #0355a3;
    --mist: #85cae6;
    --rule: #3176b5;
    --white: #ffffff;
    --label: #a8a8a8;
    --page: #ffffff;
  }
  * { box-sizing: border-box; margin: 0; padding: 0; }
  html, body { width: 1200px; height: 467px; overflow: hidden; background: var(--page); }
  body { position: relative; font-family: "Jost", sans-serif; }

  .side-label {
    position: absolute; top: 56px; width: 500px; text-align: center;
    font-size: 26px; font-weight: 400; color: var(--label); letter-spacing: 1px;
  }
  .side-label--front { left: 72px; }
  .side-label--back { left: 628px; }

  .card { position: absolute; top: 106px; width: 500px; height: 300px; overflow: hidden; }
  .card--front { left: 72px; }
  .card--back { left: 628px; }

  .band { position: absolute; left: 0; width: 100%; }
  .band--sky { top: 0; background: var(--sky); }
  .band--ocean { bottom: 0; background: var(--ocean); }
  .card--front .band--sky { height: 134px; }
  .card--front .band--ocean { height: 166px; }
  .card--back .band--sky { height: 187px; }
  .card--back .band--ocean { height: 113px; }

  .brand {
    position: absolute; display: flex; align-items: center; gap: 12px;
    color: var(--white); font-weight: 700; white-space: nowrap; letter-spacing: 0.5px;
  }
  .brand__dot { border-radius: 50%; background: var(--white); flex: none; }
  .card--front .brand { left: 78px; top: 46px; font-size: 34px; }
  .card--front .brand__dot { width: 40px; height: 40px; }
  .card--back .brand { left: 0; width: 100%; justify-content: center; top: 80px; font-size: 44px; }

  .accent-bar { position: absolute; height: 26px; background: var(--sky); }
  .accent-bar--name { left: 0; top: 202px; width: 60px; }
  .accent-bar--left { left: 0; top: 231px; width: 87px; }
  .accent-bar--right { right: 0; top: 231px; width: 89px; }

  .person-name {
    position: absolute; left: 70px; top: 199px;
    font-size: 21px; font-weight: 500; color: var(--white);
  }

  .contact-list { position: absolute; left: 260px; top: 160px; width: 240px; list-style: none; }
  .contact-item {
    position: relative; display: flex; align-items: flex-start; gap: 10px;
    padding: 4px 0 5px 0; border-bottom: 1px solid var(--rule);
    font-size: 12px; line-height: 15px; color: var(--white);
  }
  .contact-item:last-child { border-bottom: 1px solid var(--rule); }
  .contact-icon {
    flex: none; width: 18px; height: 18px; border-radius: 50%;
    border: 1px solid var(--mist); display: flex; align-items: center; justify-content: center;
  }
  .contact-icon svg { width: 10px; height: 10px; fill: var(--white); }
  .contact-text { padding-top: 1px; }

  .web-address {
    position: absolute; left: 0; width: 100%; top: 233px; text-align: center;
    font-size: 17px; font-weight: 500; color: var(--white); letter-spacing: 4px;
  }
</style>
</head>
<body>
  <div class="side-label side-label--front">FRONT</div>
  <div class="side-label side-label--back">BACK</div>

  <section class="card card--front" aria-label="Card front">
    <div class="band band--sky"></div>
    <div class="band band--ocean"></div>
    <div class="brand"><span class="brand__dot"></span>ROAM QUILL</div>

    <div class="accent-bar accent-bar--name"></div>
    <div class="person-name">Bertrand Olesky</div>

    <ul class="contact-list">
      <li class="contact-item">
        <span class="contact-icon"><svg viewBox="0 0 10 10"><path d="M2 0.5 L3.6 2.6 L2.8 3.6 Q3.8 5.6 6.2 7 L7.2 6.2 L9.4 7.8 L8.4 9.4 Q4.6 9.4 0.6 3.4 Z"/></svg></span>
        <span class="contact-text">+1-(345)-402-7731</span>
      </li>
      <li class="contact-item">
        <span class="contact-icon"><svg viewBox="0 0 10 10"><rect x="0.5" y="2" width="9" height="6"/><path d="M0.5 2 L5 5.5 L9.5 2" stroke="#0355a3" stroke-width="0.9" fill="none"/></svg></span>
        <span class="contact-text">ceo@roamquill.net</span>
      </li>
      <li class="contact-item">
        <span class="contact-icon"><svg viewBox="0 0 10 10"><circle cx="5" cy="5" r="4.5"/><path d="M0.5 5 H9.5 M5 0.5 V9.5" stroke="#0355a3" stroke-width="0.8"/><ellipse cx="5" cy="5" rx="2" ry="4.5" fill="none" stroke="#0355a3" stroke-width="0.8"/></svg></span>
        <span class="contact-text">www.roamquill.net</span>
      </li>
      <li class="contact-item">
        <span class="contact-icon"><svg viewBox="0 0 10 10"><path d="M5 0.3 A3.4 3.4 0 0 1 8.4 3.7 C8.4 6 5 9.7 5 9.7 C5 9.7 1.6 6 1.6 3.7 A3.4 3.4 0 0 1 5 0.3 Z"/><circle cx="5" cy="3.7" r="1.3" fill="#0355a3"/></svg></span>
        <span class="contact-text">Coral Reach Shore, Grand<br>Cayman, Cayman Islands</span>
      </li>
    </ul>
  </section>

  <section class="card card--back" aria-label="Card back">
    <div class="band band--sky"></div>
    <div class="band band--ocean"></div>
    <div class="brand">ROAM QUILL</div>
    <div class="accent-bar accent-bar--left"></div>
    <div class="accent-bar accent-bar--right"></div>
    <div class="web-address">www.roamquill.net</div>
  </section>
</body>
</html>
```